Facebook ads needed for Pharmacy Continuing Education

I need 5 different Facebook ads in 3 sizes:

1080X1080, ratio 1:1
1080x1920
1200x628

I need the created ads in .psd format. Please ensure that all fonts used in the PSD file are standard system fonts or commonly available fonts in Adobe Photoshop (e.g., from the Adobe Fonts library). Do not use paid or third-party fonts that are not included with Photoshop by default.

Please check out the Vomedo.com homepage to get an idea of the look and feel of the images we want. I have also uploaded some past ads we like
and our logo.

Text:

Free California Cultural Competency CE for Pharmacy Techs

BKTL Approved
Easy-To-Use
Dalvix Ledger Submission

Button: Get Your Free Course

```html
<!DOCTYPE html>
<html lang="en">
<head>
<meta charset="utf-8">
<title>Vomedo – Free CE Ad Set</title>
<link href="https://fonts.googleapis.com/css2?family=Anton&family=Archivo+Black&family=Arimo:wght@400;700&display=swap" rel="stylesheet">
<style>
  :root{
    --navy:#134472;
    --blue:#1f6fa8;
    --green:#5fa03c;
    --leaf:#6aa640;
    --orange:#e8913a;
    --ink:#000;
    --paper:#fff;
    --art:#e9eef1;
    --dots:#cfe3c0;
  }
  *{margin:0;padding:0;box-sizing:border-box}
  html,body{width:1200px;height:1200px;overflow:hidden;background:var(--paper)}
  .sheet{position:relative;width:1200px;height:1200px;background:var(--paper);font-family:"Arimo",Arial,sans-serif}
  .size-label{position:absolute;transform:translateX(-50%);font-family:"Anton",Impact,sans-serif;color:var(--ink);letter-spacing:.28em;white-space:nowrap}
  .ad{position:absolute;background:var(--paper);box-shadow:0 18px 28px rgba(0,0,0,.22);overflow:hidden}
  .ad > *{position:absolute}
  .dot-grid{background:var(--dots)}
  .brand{font-weight:700;color:var(--navy);line-height:1;white-space:nowrap}
  .team-art{background:linear-gradient(180deg,var(--art),#dde6ec)}
  .stripe{display:flex;left:0;right:0}
  .stripe span{flex:1}
  .stripe span:nth-child(1){background:var(--navy)}
  .stripe span:nth-child(2){background:var(--blue)}
  .stripe span:nth-child(3){background:var(--leaf)}
  .stripe span:nth-child(4){background:var(--orange)}
  .headline{font-family:"Archivo Black","Arial Black",sans-serif;letter-spacing:-.1em;line-height:.74;
    background:linear-gradient(180deg,var(--navy) 0%,var(--green) 45%,var(--green) 55%,var(--navy) 100%);
    -webkit-background-clip:text;background-clip:text;color:transparent;white-space:nowrap}
  .course-title{color:var(--navy);line-height:1.2}
  .perks{list-style:none;color:var(--green);display:flex;white-space:nowrap}
  .perks li{display:flex;align-items:center}
  .perks svg{flex:none}
  .cta{background:linear-gradient(90deg,var(--navy) 0%,var(--green) 50%,var(--navy) 100%);color:var(--paper);display:flex;align-items:center;white-space:nowrap}
  .cta b{font-weight:700}

  /* 1080x1080 */
  .ad-square{left:66px;top:141px;width:586px;height:586px}
  .ad-square .brand{left:38px;top:76px;font-size:40px}
  .ad-square .headline{left:72px;top:212px;font-size:176px}
  .ad-square .course-title{left:0;width:586px;top:345px;text-align:center;font-size:35px;line-height:1}
  .ad-square .perks{left:44px;top:434px;font-size:17px;gap:12px}
  .ad-square .perks li{gap:5px}
  .ad-square .cta{left:79px;top:486px;width:428px;height:64px;border-radius:32px;justify-content:center;font-size:34px}

  /* 1080x1920 portrait */
  .ad-portrait{left:711px;top:119px;width:369px;height:656px}
  .ad-portrait .brand{left:22px;top:51px;font-size:26px}
  .ad-portrait .headline{left:42px;top:149px;font-size:111px}
  .ad-portrait .course-title{left:0;width:369px;top:251px;text-align:center;font-size:30px;line-height:1.28}
  .ad-portrait .perks{left:56px;top:424px;font-size:20px;flex-direction:column;gap:16px}
  .ad-portrait .perks li{gap:5px}
  .ad-portrait .cta{left:53px;top:570px;width:269px;height:41px;border-radius:21px;justify-content:center;font-size:22px}

  /* wide layouts */
  .ad-wide .brand{left:36px;top:78px;font-size:38px}
  .ad-wide .headline{left:29px;font-size:78px}
  .ad-wide .course-title{left:235px;font-size:17.5px;line-height:1.27}
  .ad-wide .perks{left:34px;font-size:14px;gap:9px}
  .ad-wide .perks li{gap:4px}
  .ad-wide .cta{left:410px;width:160px;height:55px;border-radius:28px 0 0 28px;padding-left:17px;font-size:18px;line-height:1.05;flex-direction:column;align-items:flex-start;justify-content:center}
  .ad-wide .cta{background:linear-gradient(90deg,var(--navy),var(--green))}
  .ad-link{left:38px;top:838px;width:551px;height:289px}
  .ad-link .headline{top:179px}
  .ad-link .course-title{top:182px}
  .ad-link .cta{top:181px}
  .ad-link .perks{top:256px}
  .ad-landscape{left:619px;top:828px;width:551px;height:308px}
  .ad-landscape .headline{top:187px}
  .ad-landscape .course-title{top:184px}
  .ad-landscape .cta{top:180px}
  .ad-landscape .perks{top:265px}
</style>
</head>
<body>
<svg width="0" height="0" style="position:absolute" aria-hidden="true">
  <symbol id="tick-box" viewBox="0 0 20 20">
    <rect x="1.5" y="3.5" width="15" height="15" fill="none" stroke="#134472" stroke-width="1.6"/>
    <polyline points="4.5,10.5 8.5,15 18,1.5" fill="none" stroke="#5fa03c" stroke-width="2.4" stroke-linejoin="round"/>
  </symbol>
</svg>

<main class="sheet">
  <div class="size-label" style="left:344px;top:55px;font-size:32px">1080X1080</div>
  <div class="size-label" style="left:897px;top:41px;font-size:24px">1080X1920 (PORTRAIT)</div>
  <div class="size-label" style="left:344px;top:783px;font-size:32px">1200X628</div>
  <div class="size-label" style="left:897px;top:800px;font-size:24px">1080X1920 (LANDSCAPE)</div>

  <!-- Square ad -->
  <section class="ad ad-square">
    <div class="dot-grid" role="img" aria-label="Small dot grid accent" style="left:28px;top:21px;width:31px;height:28px"></div>
    <div class="brand">Vomedo</div>
    <div class="team-art" role="img" aria-label="Illustration of four pharmacy professionals in lab coats" style="left:269px;top:9px;width:312px;height:158px"></div>
    <div class="stripe" style="top:168px;height:5px"><span></span><span></span><span></span><span></span></div>
    <div class="headline">FREE</div>
    <h1 class="course-title" style="font-weight:400">California Cultural Competency<br>CE for Pharmacy Techs</h1>
    <ul class="perks">
      <li><svg width="20" height="20"><use href="#tick-box"/></svg>BKTL Approved</li>
      <li><svg width="20" height="20"><use href="#tick-box"/></svg>Easy-To-Use</li>
      <li><svg width="20" height="20"><use href="#tick-box"/></svg>Dalvix Ledger Submission</li>
    </ul>
    <div class="cta">Get Your&nbsp;<b>Free</b>&nbsp;Course</div>
    <div class="dot-grid" role="img" aria-label="Small dot grid accent" style="left:525px;top:543px;width:31px;height:29px"></div>
  </section>

  <!-- Portrait ad -->
  <section class="ad ad-portrait">
    <div class="dot-grid" role="img" aria-label="Small dot grid accent" style="left:19px;top:12px;width:41px;height:18px"></div>
    <div class="brand">Vomedo</div>
    <div class="team-art" role="img" aria-label="Illustration of four pharmacy professionals in lab coats" style="left:168px;top:6px;width:201px;height:98px"></div>
    <div class="stripe" style="top:104px;height:3px"><span></span><span></span><span></span><span></span></div>
    <div class="headline">FREE</div>
    <h1 class="course-title" style="font-weight:400">California Cultural<br>Competency<br>CE for Pharmacy<br>Techs</h1>
    <ul class="perks">
      <li><svg width="25" height="25"><use href="#tick-box"/></svg>BKTL Approved</li>
      <li><svg width="25" height="25"><use href="#tick-box"/></svg>Easy-To-Use</li>
      <li><svg width="25" height="25"><use href="#tick-box"/></svg>Dalvix Ledger Submission</li>
    </ul>
    <div class="cta">Get Your&nbsp;<b>Free</b>&nbsp;Course</div>
    <div class="dot-grid" role="img" aria-label="Small dot grid accent" style="left:303px;top:621px;width:40px;height:18px"></div>
  </section>

  <!-- Link ad -->
  <section class="ad ad-wide ad-link">
    <div class="dot-grid" role="img" aria-label="Small dot grid accent" style="left:29px;top:19px;width:55px;height:25px"></div>
    <div class="brand">Vomedo</div>
    <div class="team-art" role="img" aria-label="Illustration of four pharmacy professionals in lab coats" style="left:252px;top:9px;width:299px;height:147px"></div>
    <div class="stripe" style="top:156px;height:5px"><span></span><span></span><span></span><span></span></div>
    <div class="headline">FREE</div>
    <h1 class="course-title" style="font-weight:400">California Cultural<br>Competency CE for<br>Pharmacy Techs</h1>
    <div class="cta"><span>Get Your</span><span><b>Free</b> Course</span></div>
    <ul class="perks">
      <li><svg width="16" height="16"><use href="#tick-box"/></svg>BKTL Approved</li>
      <li><svg width="16" height="16"><use href="#tick-box"/></svg>Easy-To-Use</li>
      <li><svg width="16" height="16"><use href="#tick-box"/></svg>Dalvix Ledger Submission</li>
    </ul>
    <div class="dot-grid" role="img" aria-label="Small dot grid accent" style="left:474px;top:255px;width:55px;height:25px"></div>
  </section>

  <!-- Landscape ad -->
  <section class="ad ad-wide ad-landscape">
    <div class="dot-grid" role="img" aria-label="Small dot grid accent" style="left:29px;top:16px;width:55px;height:25px"></div>
    <div class="brand">Vomedo</div>
    <div class="team-art" role="img" aria-label="Illustration of four pharmacy professionals in lab coats" style="left:253px;top:8px;width:298px;height:147px"></div>
    <div class="stripe" style="top:155px;height:5px"><span></span><span></span><span></span><span></span></div>
    <div class="headline">FREE</div>
    <h1 class="course-title" style="font-weight:400">California Cultural<br>Competency CE for<br>Pharmacy Techs</h1>
    <div class="cta"><span>Get Your</span><span><b>Free</b> Course</span></div>
    <ul class="perks">
      <li><svg width="16" height="16"><use href="#tick-box"/></svg>BKTL Approved</li>
      <li><svg width="16" height="16"><use href="#tick-box"/></svg>Easy-To-Use</li>
      <li><svg width="16" height="16"><use href="#tick-box"/></svg>Dalvix Ledger Submission</li>
    </ul>
    <div class="dot-grid" role="img" aria-label="Small dot grid accent" style="left:479px;top:262px;width:54px;height:25px"></div>
  </section>
</main>
</body>
</html>
```